Martial Art workout site needs web page design

We need a web page designed for our new martial art web site that presents innovated, monthly workouts, done by beautiful models
Web page should include
- a home page
- Page for the monthly workout
- Gallery page for the models (pics & video)
-Archived page for past workout
- Page to sign up for monthly updates
- Sponsor Page

Martial Art

```html
<!DOCTYPE html>
<html lang="en">
<head>
<meta charset="utf-8">
<title>Reed Calloway Martial Arts</title>
<link rel="stylesheet" href="https://fonts.googleapis.com/css2?family=Oswald:wght@300;400&family=Open+Sans:ital,wght@0,400;1,400&display=swap">
<style>
  :root {
    --brown: #8b5a33;
    --brown-dark: #6f4424;
    --ink: #333333;
    --text: #555555;
    --panel: #ffffff;
    --line: #dddddd;
    --footer: #222222;
    --page-top: #1c1c1c;
    --page-bottom: #a3a3a3;
  }
  * { margin: 0; padding: 0; box-sizing: border-box; }
  html, body { width: 1200px; height: 1166px; overflow: hidden; }
  body {
    position: relative;
    font-family: "Open Sans", Arial, sans-serif;
    background: linear-gradient(to bottom, var(--page-top) 0px, #262626 300px, #555 700px, var(--page-bottom) 1076px);
  }
  .top-rule { position: absolute; left: 0; top: 0; width: 1200px; height: 4px; background: var(--brown); }

  .main-panel {
    position: absolute; left: 120px; top: 38px; width: 960px; height: 918px;
    background: var(--panel); border-radius: 4px;
  }
  .brand { position: absolute; left: 11px; top: 20px; display: flex; align-items: center; gap: 14px; }
  .brand-mark { width: 64px; height: 64px; border-radius: 50%; background: var(--brown); }
  .brand-name { font-family: "Oswald", sans-serif; font-weight: 400; color: var(--brown); font-size: 40px; line-height: 44px; }
  .brand-sub { font-family: "Oswald", sans-serif; font-weight: 300; color: var(--ink); font-size: 36px; line-height: 38px; }

  .main-nav { position: absolute; left: 340px; top: 0; height: 110px; display: flex; }
  .main-nav a {
    font-family: "Oswald", sans-serif; font-weight: 300; font-size: 20px; color: var(--ink);
    text-decoration: none; padding: 62px 11px 0; height: 110px;
  }
  .main-nav a.active {
    color: #fff; padding: 62px 9px 0;
    background: linear-gradient(to bottom, #555 0%, #3a3a3a 100%);
    border-bottom: 9px solid var(--brown);
  }

  .hero {
    position: absolute; left: 10px; top: 125px; width: 940px; height: 377px;
    border: 2px solid #e4e4e4;
    background: radial-gradient(ellipse at 40% 40%, #7a4e3a 0%, #3a2320 45%, #1a1414 100%);
  }
  .hero-dots { position: absolute; left: 23px; top: 322px; display: flex; gap: 7px; }
  .hero-dots span { width: 18px; height: 18px; border-radius: 4px; background: #b5b5b5; }
  .hero-dots span.current { background: var(--brown); }

  .section-title { position: absolute; font-family: "Oswald", sans-serif; font-weight: 400; font-size: 23px; color: var(--brown); }
  .welcome-title { left: 11px; top: 521px; }
  .welcome-text { position: absolute; left: 11px; top: 557px; width: 545px; font-size: 12px; line-height: 23px; color: var(--text); }
  .read-more {
    position: absolute; left: 10px; top: 691px; width: 92px; height: 33px;
    background: #444; color: #fff; font-size: 12px; line-height: 33px; text-align: center;
  }
  .videos-title { left: 585px; top: 521px; }
  .video-frame {
    position: absolute; left: 586px; top: 566px; width: 364px; height: 158px;
    border: 2px solid #e4e4e4;
    background: linear-gradient(to bottom, #4e4a5a 0%, #8a6e70 55%, #b07a5a 100%);
  }
  .video-play { position: absolute; left: 155px; top: 42px; }

  .gallery-title { left: 11px; top: 737px; }
  .gallery-arrows { position: absolute; left: 905px; top: 744px; display: flex; gap: 5px; }
  .thumb {
    position: absolute; top: 779px; width: 222px; height: 124px;
    border: 1px solid var(--line); padding: 5px; background: #fff;
  }
  .thumb div { width: 100%; height: 100%; }

  .signup-panel {
    position: absolute; left: 120px; top: 970px; width: 960px; height: 88px;
    background: var(--panel); border-radius: 4px;
  }
  .signup-title { position: absolute; left: 28px; top: 12px; font-family: "Oswald", sans-serif; }
  .signup-title strong { display: block; font-weight: 400; font-size: 22px; color: var(--brown); line-height: 28px; }
  .signup-title span { display: block; font-weight: 400; font-size: 20px; color: var(--ink); line-height: 28px; }
  .email-field {
    position: absolute; left: 223px; top: 19px; width: 526px; height: 51px;
    background: #eeeeee; border: 1px solid #d2d2d2; border-radius: 4px;
    font-style: italic; font-size: 14px; color: #777; padding: 15px 20px;
  }
  .subscribe-btn {
    position: absolute; left: 770px; top: 20px; width: 150px; height: 50px; border-radius: 3px;
    background: linear-gradient(to bottom, #95643c, var(--brown-dark));
    font-family: "Oswald", sans-serif; font-size: 21px; color: #fff; text-align: center; line-height: 50px;
  }

  .site-footer { position: absolute; left: 0; top: 1076px; width: 1200px; height: 90px; background: var(--footer); }
  .copyright { position: absolute; left: 129px; top: 36px; font-size: 13px; color: #bbbbbb; letter-spacing: 0.2px; }
  .copyright em { font-style: normal; color: #c7803f; }
  .social { position: absolute; left: 962px; top: 31px; display: flex; gap: 8px; }
  .social span { width: 31px; height: 31px; border-radius: 50%; border: 3px solid #fff; }
  .social .s1 { background: #3b5a9a; }
  .social .s2 { background: #2ba6de; }
  .social .s3 { background: #cc2a2a; }
</style>
</head>
<body>
  <div class="top-rule"></div>

  <main class="main-panel">
    <div class="brand">
      <div class="brand-mark"></div>
      <div>
        <div class="brand-name">Reed Calloway</div>
        <div class="brand-sub">Martial Arts</div>
      </div>
    </div>

    <nav class="main-nav">
      <a class="active" href="#">Home</a>
      <a href="#">About us</a>
      <a href="#">Monthly Workout</a>
      <a href="#">Gallery</a>
      <a href="#">Archives</a>
      <a href="#">Sponsors</a>
      <a href="#">Contact us</a>
    </nav>

    <div class="hero" role="img" aria-label="Woman in red hand wraps throwing a high kick at a heavy bag">
      <div class="hero-dots"><span class="current"></span><span></span><span></span><span></span></div>
    </div>

    <h2 class="section-title welcome-title">Welcome to Reed Calloway</h2>
    <p class="welcome-text">Aliquam molestie, mi et imperdiet euismod, dui purus auctor tellus, et interdum lacus lectus et ante. Sed accumsan sollicitudin sapien, sit amet adipiscing turpis gravida ac. In congue, neque ac lobortis volutpat, libero mauris varius mi, vitae suscipit ipsum ligula vitae risus. Duis aliquam nibh a dui iaculis viverra id a velit. Vivamus egestas risus in magna varius commodo. Sed semper viverra egestas. Etiam pretium porttitor lectus, vel ornare neque porta volutpat.</p>
    <div class="read-more">Read More</div>

    <h2 class="section-title videos-title">Videos</h2>
    <div class="video-frame" role="img" aria-label="Video still of two martial artists leaping in silhouette against a sunset">
      <svg class="video-play" width="52" height="52" viewBox="0 0 52 52">
        <circle cx="26" cy="26" r="25" fill="rgba(255,255,255,0.85)"/>
        <path d="M20 15 L37 26 L20 37 Z" fill="#444"/>
      </svg>
    </div>

    <h2 class="section-title gallery-title">Photo Gallery</h2>
    <div class="gallery-arrows">
      <svg width="20" height="20" viewBox="0 0 20 20"><circle cx="10" cy="10" r="10" fill="#333"/><path d="M11.5 6 L7.5 10 L11.5 14" stroke="#fff" stroke-width="2" fill="none"/></svg>
      <svg width="20" height="20" viewBox="0 0 20 20"><circle cx="10" cy="10" r="10" fill="#333"/><path d="M8.5 6 L12.5 10 L8.5 14" stroke="#fff" stroke-width="2" fill="none"/></svg>
    </div>
    <div class="thumb" style="left:9px"><div role="img" aria-label="Two men in blue uniforms sparring on the mat" style="background:linear-gradient(to bottom,#e8ecf2,#3a5fa8 60%,#2b4a8a)"></div></div>
    <div class="thumb" style="left:249px"><div role="img" aria-label="Three people in a low martial arts stance" style="background:linear-gradient(to bottom,#f4f4f4 55%,#4a4a5a 80%,#2e2e3e)"></div></div>
    <div class="thumb" style="left:489px"><div role="img" aria-label="Student in white uniform kicking a red pad" style="background:linear-gradient(to right,#c43a3a,#e8e8e8 40%,#d8d8d8)"></div></div>
    <div class="thumb" style="left:729px"><div role="img" aria-label="Instructor demonstrating a hold in a bright studio" style="background:linear-gradient(to bottom,#e8d890,#b8a878 50%,#3a4060)"></div></div>
  </main>

  <section class="signup-panel">
    <div class="signup-title"><strong>Sign Up</strong><span>for monthly updates</span></div>
    <div class="email-field">Enter Email Address</div>
    <div class="subscribe-btn">SUBSCRIBE</div>
  </section>

  <footer class="site-footer">
    <p class="copyright">Copyright © 2013. <em>Reed Calloway.</em> All Right Reserved</p>
    <div class="social" aria-label="Social links"><span class="s1"></span><span class="s2"></span><span class="s3"></span></div>
  </footer>
</body>
</html>
```